Business card for STEADYWAVE

Please design professional business card for IT consulting firm STEADYWAVE INC.
Use logo attached.
Use information from sample qNode business card attached.
replace qnode inc with STEADYWAVE INC.
as well as qnodeinc.com with steadywave.example

```html
<!DOCTYPE html>
<html lang="en">
<head>
<meta charset="utf-8">
<title>STEADYWAVE business card</title>
<link rel="stylesheet" href="https://fonts.googleapis.com/css2?family=Montserrat:wght@700&family=Open+Sans:wght@400;600&display=swap">
<style>
  :root {
    --backdrop: #1c1c1e;
    --card: #111112;
    --white: #f4f4f4;
    --silver: #9a9a9c;
    --teal: #5ecfae;
    --cyan: #4cc3ea;
    --purple: #7a34a8;
    --orange: #f59a1f;
  }
  * { margin: 0; padding: 0; box-sizing: border-box; }
  html, body { width: 1200px; height: 900px; overflow: hidden; background: var(--backdrop); }
  .stage { position: relative; width: 1200px; height: 900px; }
  .card {
    position: absolute; left: 280px; width: 640px; height: 366px;
    background: var(--card); overflow: hidden;
    box-shadow: 0 18px 40px rgba(0,0,0,.55);
  }
  .card--front { top: 50px; }
  .card--back { top: 480px; }
  .card__edge {
    position: absolute; left: 0; right: 0; bottom: 0; height: 7px;
    background: linear-gradient(90deg, var(--purple), #5d8fb8 28%, var(--teal) 48%, var(--cyan) 70%, var(--orange));
  }
  .wordmark {
    position: absolute; font-family: "Montserrat", sans-serif; font-weight: 700;
    color: var(--white); letter-spacing: .12em; line-height: 1;
  }
  .card--front .wordmark { left: 36px; top: 34px; font-size: 44px; }
  .card--back .wordmark { left: 0; right: 0; top: 160px; text-align: center; font-size: 50px; color: var(--silver); }
  .person { position: absolute; left: 40px; top: 108px; font-family: "Open Sans", sans-serif; }
  .person__name { color: var(--teal); font-weight: 600; font-size: 19px; letter-spacing: .03em; text-transform: uppercase; }
  .person__title { color: var(--white); font-size: 15px; margin-top: 2px; }
  .divider { position: absolute; left: 40px; right: 40px; top: 166px; height: 1px; background: var(--purple); }
  .contacts { position: absolute; left: 40px; top: 184px; list-style: none; font-family: "Open Sans", sans-serif; font-size: 15px; color: var(--white); }
  .contacts li { display: flex; align-items: center; gap: 9px; line-height: 25px; }
  .contacts svg { width: 14px; height: 14px; fill: none; stroke: var(--cyan); stroke-width: 2; }
  .office { position: absolute; right: 40px; top: 232px; text-align: right; font-family: "Open Sans", sans-serif; font-size: 15px; line-height: 22px; color: var(--white); }
  .office__company { color: var(--cyan); text-transform: uppercase; }
</style>
</head>
<body>
<main class="stage">
  <section class="card card--front">
    <div class="wordmark">STEADYWAVE</div>
    <div class="person">
      <div class="person__name">Daniel Marlow, P.Eng.</div>
      <div class="person__title">General Manager</div>
    </div>
    <div class="divider"></div>
    <ul class="contacts">
      <li><svg viewBox="0 0 16 16"><path d="M4 1.5l2.5 3-1.5 2a9 9 0 004.5 4.5l2-1.5 3 2.5-1.5 2.5C7 14 2 9 1.5 3z"/></svg>(555) 214-3080 ext.201</li>
      <li><svg viewBox="0 0 16 16"><rect x="4" y="1" width="8" height="14" rx="1.5"/><path d="M7 12.5h2"/></svg>(555) 730-4192</li>
      <li><svg viewBox="0 0 16 16"><rect x="1.5" y="3.5" width="13" height="9"/><path d="M1.5 3.5L8 9l6.5-5.5"/></svg>dmarlow@steadywave.example</li>
      <li><svg viewBox="0 0 16 16"><circle cx="8" cy="8" r="6.5"/><path d="M1.5 8h13M8 1.5c-3 3.5-3 9.5 0 13M8 1.5c3 3.5 3 9.5 0 13"/></svg>www.steadywave.example</li>
    </ul>
    <address class="office" style="font-style:normal">
      <div class="office__company">STEADYWAVE INC.</div>
      <div>1820 Harbourline RD, Suite 101</div>
      <div>Oakridge, Ontario</div>
      <div>L4K 2P9, Canada</div>
    </address>
    <div class="card__edge"></div>
  </section>
  <section class="card card--back">
    <div class="wordmark">STEADYWAVE</div>
    <div class="card__edge"></div>
  </section>
</main>
</body>
</html>
```